Presentation Folder for Crest Holdings

We are a new property management / real estate company in Denver Colorado and are in need of new stationary design. Attached are our business card and logo deigns. We are looking for our stationary design. We need a presentation folder design that is Professional, exciting, and approachable. We do not have a preference on folder layout (pockets, style of folding) but will most likely be using a standard two pocket folder design (roughly 9x12) but feel free to experiment with and folder style as long as we can find a place to print them. We would also like to have a matching letterhead/page design
Below is standard size of folder from plume press
Full Bleed Size
20.87" x 16.68"
53 x 42.4 cm
6260 x 5004 pixels
Document Trim Size
20.75" x 16.56"
52.7 x 42.1 cm
6225 x 4969 pixels
Target Market(s)
We are attempting to target the top end of the real estate market in Denver Colorado. Are target market is investors in real estate.
Industry/Entity Type
Property Management
Font styles to use
Other font styles liked:
- Would like to keep font same to logo
Look and feel
Each slider illustrates characteristics of the customer's brand and the style your logo design should communicate.

```html
<!DOCTYPE html>
<html lang="en">
<head>
<meta charset="utf-8">
<title>Crest Holdings — Presentation Folder</title>
<link rel="stylesheet" href="https://fonts.googleapis.com/css2?family=Oswald:wght@500&family=Open+Sans:ital,wght@0,400;1,400&display=swap">
<style>
  :root {
    --backdrop: #1f4650;
    --brand-blue: #63adc9;
    --brand-blue-deep: #4f97b4;
    --paper: #ffffff;
    --paper-shade: #eceef0;
    --ink-grey: #6d6e70;
    --fold-line: #d5d9dc;
  }
  html, body {
    margin: 0;
    width: 1200px;
    height: 802px;
    overflow: hidden;
    background: var(--backdrop);
  }
  .folder-layout {
    display: block;
    width: 1200px;
    height: 802px;
  }
  .brand-name {
    font-family: "Oswald", sans-serif;
    font-weight: 500;
    fill: var(--ink-grey);
    letter-spacing: 0.5px;
  }
  .brand-name--cover {
    fill: var(--brand-blue);
  }
  .brand-tagline {
    font-family: "Open Sans", sans-serif;
    font-style: italic;
    fill: var(--ink-grey);
  }
</style>
</head>
<body>
<svg class="folder-layout" viewBox="0 0 1200 802" xmlns="http://www.w3.org/2000/svg">
  <defs>
    <linearGradient id="inner-flap" x1="0" y1="0" x2="0" y2="1">
      <stop offset="0" stop-color="var(--brand-blue)"/>
      <stop offset="1" stop-color="var(--brand-blue-deep)"/>
    </linearGradient>
    <linearGradient id="paper-face" x1="0" y1="0" x2="1" y2="1">
      <stop offset="0" stop-color="var(--paper)"/>
      <stop offset="1" stop-color="var(--paper-shade)"/>
    </linearGradient>
    <clipPath id="cover-clip">
      <rect x="0" y="0" width="438.5" height="700"/>
    </clipPath>
  </defs>

  <!-- outer front cover -->
  <g class="outer-cover" transform="translate(30,114) scale(0.821)">
    <rect class="cover-face" x="0" y="0" width="438.5" height="700" fill="url(#paper-face)"/>
    <g clip-path="url(#cover-clip)">
      <circle class="cover-disc" cx="300" cy="230" r="200" fill="var(--brand-blue)"/>
    </g>
    <text class="brand-name brand-name--cover" x="36" y="640" font-size="36">CREST HOLDINGS</text>
    <text class="brand-tagline" x="37" y="664" font-size="12">Property Management and Real Estate</text>
  </g>

  <!-- inside spread -->
  <g class="inside-spread" transform="translate(430,114) scale(0.821)">
    <rect class="panel-left" x="0" y="0" width="438.5" height="700" fill="url(#inner-flap)"/>
    <rect class="panel-right" x="438.5" y="0" width="438.5" height="700" fill="url(#paper-face)"/>
    <line class="spine" x1="438.5" y1="0" x2="438.5" y2="700" stroke="var(--fold-line)" stroke-width="1"/>

    <polygon class="pocket-left" points="0,490 399,480 438.5,700 0,700" fill="url(#paper-face)" stroke="var(--fold-line)" stroke-width="1"/>
    <polygon class="pocket-right" points="438.5,700 519,510 877,490 877,700" fill="url(#paper-face)" stroke="var(--fold-line)" stroke-width="1"/>

    <circle class="brand-dot" cx="199" cy="579" r="14" fill="var(--brand-blue)"/>
    <text class="brand-name" x="199" y="631" font-size="30" text-anchor="middle">CREST HOLDINGS</text>
    <text class="brand-tagline" x="199" y="650" font-size="11" text-anchor="middle">Property Management and Real Estate</text>

    <circle class="brand-dot" cx="657" cy="211" r="30" fill="var(--brand-blue)"/>
    <text class="brand-name" x="657" y="284" font-size="28" text-anchor="middle">CREST HOLDINGS</text>
  </g>
</svg>
</body>
</html>
```